Modern and Elegant business card

A clean and modern but traditional business card is required to reflect the updated LOGO and the new website www.brivexalta.com

The old card as provided is a bit disjointed, crowded and not clear to read especially the company name which is almost hidden in the logo.

The card should take it's queues from the colours of the logo which are green, yellow and orange, bold but rich, not faded or washed out.

We are looking to drastically clean up and improve our old cards

Target Market(s)

Professional Consulting and Business/Government

Industry/Entity Type

Management Consulting

Contact Information for Business Card

The card needs to outlined the new Service Groups as seen on the new site: http://brivexalta.com/services/ New logo needs to be included
The usual info for phones, address and name and email

Font styles to use
Serif
Sans Serif

Colors
fbee3d
f78f20
9bcb3c

Requirements
Must have
• New logo as seen on the current site and provided here
• Service Groups as seen http://brivexalta.com/services/
• Needs to be functional and clean, well proportioned and organized
Nice to have
• Name of cities where offices are located

```html
<!DOCTYPE html>
<html lang="en">
<head>
<meta charset="utf-8">
<title>Brivexalta Business Card</title>
<link href="https://fonts.googleapis.com/css2?family=Crimson+Text:wght@400;600&display=swap" rel="stylesheet">
<style>
  :root {
    --stage: #2b2b2d;
    --paper: #ffffff;
    --sun-yellow: #fbee3d;
    --sun-gold: #fbc02d;
    --sun-orange: #f78f20;
    --deep-orange: #ef6a2c;
    --ink: #2a2a2a;
    --ink-soft: #555555;
    --rule: #d9d9d9;
  }
  * { box-sizing: border-box; margin: 0; padding: 0; }
  html, body {
    width: 1200px; height: 660px; overflow: hidden;
    background: var(--stage);
    font-family: "Crimson Text", Georgia, serif;
  }
  .stage {
    width: 1200px; height: 660px;
    display: flex; align-items: center; justify-content: center; gap: 50px;
  }
  .card {
    width: 525px; height: 300px; position: relative; overflow: hidden;
    box-shadow: 0 12px 30px rgba(0,0,0,.55);
  }

  /* Front */
  .card-front {
    background: linear-gradient(160deg, var(--sun-yellow) 0%, var(--sun-gold) 35%, var(--sun-orange) 70%, var(--deep-orange) 100%);
    display: flex; align-items: center; justify-content: center; gap: 14px;
  }
  .front-mark {
    width: 22px; height: 22px; border-radius: 50%; background: var(--paper);
  }
  .front-name {
    color: var(--paper); font-size: 52px; font-weight: 400;
    letter-spacing: 3px; text-transform: uppercase;
  }

  /* Back */
  .card-back { background: var(--paper); }
  .back-brand {
    position: absolute; top: 26px; left: 150px;
    display: flex; align-items: center; gap: 7px;
  }
  .back-brand-mark { width: 10px; height: 10px; border-radius: 50%; background: var(--sun-orange); }
  .back-brand-name {
    font-size: 21px; color: var(--ink); letter-spacing: 1.5px; text-transform: uppercase;
  }
  .contact {
    position: absolute; top: 72px; left: 24px; width: 250px; text-align: right;
    color: var(--ink);
  }
  .contact-name {
    font-size: 17px; font-weight: 600; letter-spacing: 1px; text-transform: uppercase; line-height: 1.1;
  }
  .contact-title { font-size: 12px; color: var(--ink-soft); line-height: 1.25; margin-right: 22px; }
  .contact-lines { margin-top: 6px; list-style: none; }
  .contact-lines li {
    font-size: 12.5px; line-height: 17px;
    display: flex; justify-content: flex-end; align-items: center; gap: 7px;
  }
  .contact-lines svg { width: 12px; height: 12px; flex: none; }
  .contact-lines .no-icon { padding-right: 19px; }
  .divider {
    position: absolute; top: 62px; left: 288px; width: 1px; height: 170px; background: var(--rule);
  }
  .services {
    position: absolute; top: 64px; left: 302px; list-style: none; color: var(--ink);
  }
  .services li {
    font-size: 12.5px; line-height: 16px; padding-left: 12px; position: relative; margin-bottom: 2px;
  }
  .services li::before {
    content: ""; position: absolute; left: 0; top: 6px;
    width: 4px; height: 4px; border-radius: 50%; background: var(--deep-orange);
  }
  .band-line {
    position: absolute; left: 0; right: 0; bottom: 30px; height: 3px; background: var(--sun-yellow);
  }
  .band-fill {
    position: absolute; left: 0; right: 0; bottom: 0; height: 24px;
    background: linear-gradient(90deg, var(--sun-orange), var(--deep-orange));
  }
</style>
</head>
<body>
<main class="stage">
  <section class="card card-front" aria-label="Card front">
    <span class="front-mark"></span>
    <span class="front-name">Brivexalta</span>
  </section>

  <section class="card card-back" aria-label="Card back">
    <div class="back-brand">
      <span class="back-brand-mark"></span>
      <span class="back-brand-name">Brivexalta</span>
    </div>

    <div class="contact">
      <p class="contact-name">Dara Kelmont</p>
      <p class="contact-title">Senior Partner, Western Canada</p>
      <p class="contact-title">Chief Operating Officer</p>
      <ul class="contact-lines">
        <li>(780) 555-0142
          <svg viewBox="0 0 12 12"><rect x="3" y="1" width="6" height="10" rx="1" fill="none" stroke="#f78f20" stroke-width="1.2"/><line x1="5" y1="9" x2="7" y2="9" stroke="#f78f20"/></svg></li>
        <li>(780) 555-0187
          <svg viewBox="0 0 12 12"><path d="M2 4 Q6 0 10 4 L9 6 L7 5 L5 5 L3 6 Z" fill="#f78f20"/><rect x="3" y="7" width="6" height="4" fill="#f78f20"/></svg></li>
        <li>dara@brivexalta.com
          <svg viewBox="0 0 12 12"><rect x="1" y="3" width="10" height="7" fill="#f78f20"/><path d="M1 3 L6 7 L11 3" fill="none" stroke="#fff" stroke-width="1"/></svg></li>
        <li>www.brivexalta.com
          <svg viewBox="0 0 12 12"><circle cx="6" cy="6" r="5" fill="none" stroke="#f78f20" stroke-width="1.2"/><ellipse cx="6" cy="6" rx="2" ry="5" fill="none" stroke="#f78f20"/><line x1="1" y1="6" x2="11" y2="6" stroke="#f78f20"/></svg></li>
        <li class="no-icon">4120 - 88B Street NW</li>
        <li class="no-icon">Calderon AB Canada T2X 4R7</li>
      </ul>
    </div>

    <div class="divider"></div>

    <ul class="services">
      <li>Export Market Development</li>
      <li>Business Strategy</li>
      <li>Energy Sector Strategy</li>
      <li>Community And<br>Economic Development</li>
      <li>Commercial/Retail Business</li>
      <li>Optimization Strategy</li>
      <li>Strategic Communications<br>Branding and Social Media</li>
    </ul>

    <div class="band-line"></div>
    <div class="band-fill"></div>
  </section>
</main>
</body>
</html>
```